Business Card Design Project

looking for business cards with new logo

I am looking to keep with the colors of the logo i posted.  Here are some other details to consider.  I would like my website prominently displayed on the business card with the logo.  my website is www.HavenrockTX.com...it should be spelled this way.

My contact information is:

Daniel P Whitcomb III
Broker/Owner
48391 Cordell Ave., Suite 307
Helotes, Texas 78023
Office: 210-555-0147
Email:  Daniel@HavenrockTX.com

Thank you
Daniel Whitcomb

```html
<!DOCTYPE html>
<html lang="en">
<head>
<meta charset="utf-8">
<title>Havenrock Realty — Business Cards</title>
<link rel="stylesheet" href="https://fonts.googleapis.com/css2?family=Open+Sans:wght@400;600;700&display=swap">
<style>
  :root {
    --backdrop: #d3cdc7;
    --card-black: #1d1d1e;
    --card-white: #ffffff;
    --tab-white: #f4f4f4;
    --brand-blue: #4fa3de;
    --ink-dark: #2b2b2d;
    --ink-soft: #6a6a6e;
    --watermark: #ececee;
  }
  * { box-sizing: border-box; margin: 0; padding: 0; }
  html, body { width: 1200px; height: 800px; overflow: hidden; }
  body {
    background: var(--backdrop);
    font-family: "Open Sans", Arial, sans-serif;
    position: relative;
  }
  .card {
    position: absolute;
    top: 252px;
    width: 520px;
    height: 297px;
    overflow: hidden;
    box-shadow: 0 6px 18px rgba(0,0,0,0.18);
  }
  .card--front { left: 40px; background: var(--card-black); }
  .card--back  { left: 640px; background: var(--card-white); }

  .corner-tabs { position: absolute; inset: 0; }

  .brand {
    position: absolute;
    left: 0; right: 0;
    display: flex;
    align-items: center;
    justify-content: center;
    gap: 12px;
    font-weight: 600;
    letter-spacing: 0.5px;
  }
  .brand__mark { width: 14px; height: 14px; background: var(--brand-blue); }
  .card--front .brand { top: 92px; font-size: 42px; color: #ffffff; }
  .card--back  .brand { top: 24px; font-size: 26px; color: var(--ink-dark); }
  .card--back  .brand__mark { width: 10px; height: 10px; }

  .website {
    position: absolute;
    top: 190px; left: 0; right: 0;
    text-align: center;
    color: #ffffff;
    font-size: 19px;
    font-weight: 600;
  }
  .website__name { color: var(--brand-blue); }

  .contact {
    position: absolute;
    top: 92px; left: 0; right: 0;
    text-align: center;
    color: var(--ink-soft);
    font-size: 12px;
    line-height: 1.55;
  }
  .contact__name { color: var(--brand-blue); font-size: 15px; font-weight: 700; }
  .contact__role { font-weight: 600; color: var(--ink-dark); margin-bottom: 4px; }

  .watermark {
    position: absolute;
    right: -20px; bottom: -14px;
    font-size: 78px;
    font-weight: 600;
    color: var(--watermark);
    white-space: nowrap;
  }
</style>
</head>
<body>
  <section class="card card--front">
    <svg class="corner-tabs" width="520" height="297" viewBox="0 0 520 297" aria-hidden="true">
      <polygon points="0,0 46,0 22,24 22,273 46,297 0,297" fill="var(--tab-white)"/>
      <polygon points="520,0 474,0 498,24 498,273 474,297 520,297" fill="var(--tab-white)"/>
    </svg>
    <div class="brand"><span class="brand__mark"></span><span>Havenrock Realty</span></div>
    <p class="website">www.<span class="website__name">HavenrockTX</span>.com</p>
  </section>

  <section class="card card--back">
    <div class="watermark">Havenrock Realty</div>
    <div class="brand"><span class="brand__mark"></span><span>Havenrock Realty</span></div>
    <div class="contact">
      <p class="contact__name">Daniel P Whitcomb III</p>
      <p class="contact__role">Broker/Owner</p>
      <p>48391 Cordell Ave., Suite 307</p>
      <p>Helotes, Texas 78023</p>
      <p>Office: 210-555-0147</p>
      <p>Email: Daniel@HavenrockTX.com</p>
    </div>
  </section>
</body>
</html>
```